Fernwillow needs product labels for deodorant line, and future soap, and lip balm line.

Fernwillow is a new startup that at this time is looking for labels for our deodorant line. There will be future work for our other products given to the winning designer. Our products are all-natural free from petrochemicals, propylene glycol, parabens, aluminum compounds, or synthetic colorants. All our products are also handmade.
We are using a standard size stick to contain the product, on the front cap the label is 2"W x 1"H, on the body front and back the size is 2" W x 2.675" H. We want the front to say "aluminum free", and "all-natural deodorant"
The back needs to include, a UPC, Our mission is to bring you effective, all-natural products using the highest quality ingredients. , Ingredients Cocoa Butter, Shea Butter, Arrowroot Powder, Sodium Bicarbonate, Olive Oil, Water.
We are launching 4 scents.
scent free
Lavander
Tea Tree
Baby Powder
We included a couple pics of product labels we like but are definitely not limited to them. also a picture of the empty container.
Updates
Project Deadline Extended
Reason: Someone completed their design but didn't post it in time and asked me to extend the dead line.
Target Market(s)
Females that are health conscience.
Industry/Entity Type
Cosmetics

```html
<!DOCTYPE html>
<html lang="en">
<head>
<meta charset="utf-8">
<title>Fernwillow – Deodorant Labels</title>
<link rel="stylesheet" href="https://fonts.googleapis.com/css2?family=Open+Sans:ital,wght@0,400;1,400&display=swap">
<style>
  :root {
    --page: #ffffff;
    --ink-light: #ffffff;
    --scentfree: #f754a8;
    --scentfree-ink: #a3143f;
    --scentfree-art: #fbb7d8;
    --powder: #5a95c5;
    --powder-ink: #173f6b;
    --powder-art: #b5cfe6;
    --lavender: #991f87;
    --lavender-ink: #4e0f47;
    --lavender-art: #c27bb9;
    --teatree: #1a9134;
    --teatree-ink: #0e5a22;
    --teatree-art: #8fd08a;
  }
  * { box-sizing: border-box; margin: 0; padding: 0; }
  html, body {
    width: 959px; height: 1200px; overflow: hidden;
    background: var(--page);
  }
  body {
    position: relative;
    font-family: "Open Sans", Arial, sans-serif;
  }
  .label {
    position: absolute;
    width: 417px; height: 558px;
    border-radius: 10px;
    background: var(--bg);
  }
  .label--scentfree { left: 47px;  top: 29px;  --bg: var(--scentfree); --ink: var(--scentfree-ink); --art: var(--scentfree-art); }
  .label--powder    { left: 501px; top: 29px;  --bg: var(--powder);    --ink: var(--powder-ink);    --art: var(--powder-art); }
  .label--lavender  { left: 49px;  top: 615px; --bg: var(--lavender);  --ink: var(--lavender-ink);  --art: var(--lavender-art); }
  .label--teatree   { left: 501px; top: 615px; --bg: var(--teatree);   --ink: var(--teatree-ink);   --art: var(--teatree-art); }

  .label__frame {
    position: absolute; inset: 12px;
    border: 3px solid var(--ink-light);
    border-radius: 14px;
  }
  .label__art {
    position: absolute;
    left: 108px; top: 45px;
    width: 200px; height: 180px;
    border-radius: 50%;
    background: radial-gradient(circle, var(--art) 0%, var(--art) 35%, transparent 72%);
    opacity: 0.85;
  }
  .label__brand {
    position: absolute; left: 0; right: 0; top: 270px;
    text-align: center;
    color: var(--ink-light);
    font-size: 50px; font-weight: 400;
    letter-spacing: 0.5px;
  }
  .label__claim {
    position: absolute; left: 0; right: 0;
    text-align: center;
    color: var(--ink-light);
    font-size: 19px;
  }
  .label__claim--natural { top: 372px; }
  .label__claim--aluminum { top: 413px; }
  .label__scent {
    position: absolute; left: 0; right: 0; top: 451px;
    text-align: center;
    color: var(--ink);
    font-size: 33px; font-style: italic;
  }
</style>
</head>
<body>

  <section class="label label--scentfree">
    <div class="label__frame"></div>
    <div class="label__art" role="img" aria-label="Soft pale pink flower with small leafy sprigs"></div>
    <p class="label__brand">Fernwillow</p>
    <p class="label__claim label__claim--natural">All natural deodorant</p>
    <p class="label__claim label__claim--aluminum">Aluminum free</p>
    <p class="label__scent">scent -free</p>
  </section>

  <section class="label label--powder">
    <div class="label__frame"></div>
    <div class="label__art" role="img" aria-label="Scattered pale blue powder puffs"></div>
    <p class="label__brand">Fernwillow</p>
    <p class="label__claim label__claim--natural">All natural deodorant</p>
    <p class="label__claim label__claim--aluminum">Aluminum free</p>
    <p class="label__scent">baby powder</p>
  </section>

  <section class="label label--lavender">
    <div class="label__frame"></div>
    <div class="label__art" role="img" aria-label="Bunch of lilac lavender sprigs"></div>
    <p class="label__brand">Fernwillow</p>
    <p class="label__claim label__claim--natural">All natural deodorant</p>
    <p class="label__claim label__claim--aluminum">Aluminum free</p>
    <p class="label__scent">lavender</p>
  </section>

  <section class="label label--teatree">
    <div class="label__frame"></div>
    <div class="label__art" role="img" aria-label="Light green tea tree leaf sprig"></div>
    <p class="label__brand">Fernwillow</p>
    <p class="label__claim label__claim--natural">All natural deodorant</p>
    <p class="label__claim label__claim--aluminum">Aluminum free</p>
    <p class="label__scent">tea tree</p>
  </section>

</body>
</html>
```